Wordpress Design Project (Bramblewick)

We need a wordpress design for an established auction and real estate company based in New Hampshire. The winning design will incorporate the colors of logo (red and blue) creatively with black or gray in a very professional and clean layout. Client mentions liking the site http://www.veltranbids.com/ as a general idea.

Industry/Entity Type

Real Estate

Requirements
Must have
• Navigation:
1) Home (lorem text)
2) Upcoming Auctions
3) Auction Results
4) Sell or Consign
5) About Us
6) Services
7) FAQ
8) Contact Us

Site will have slideshow, initial image attached.
Sidebar widgets:
- Email sign up form
- Featured Auction (like at http://www.dorvexsalehouse.com) - - - - Video Widget
- Testimonials widget

Footer will have smaller logo, contact info, and 2 association logos (attached)
-
Nice to have
• use of drop-down menu design for 'Services'
1) Appraisals
2) Consulting
Should not have
• please use no gavels in the design

```html
<!DOCTYPE html>
<html lang="en">
<head>
<meta charset="utf-8">
<title>Bramblewick Auctions</title>
<link rel="stylesheet" href="https://fonts.googleapis.com/css2?family=Tinos:wght@400;700&family=Arimo:wght@400;700&display=swap">
<style>
:root{
  --navy:#0e1850;
  --navy-dark:#08103a;
  --red:#b01c1c;
  --red-dark:#8e1414;
  --page:#ebebeb;
  --panel:#f1f1f1;
  --line:#cfcfcf;
  --text:#4a4a4a;
  --muted:#6b6b6b;
  --bg:#161616;
}
*{box-sizing:border-box;margin:0;padding:0}
html,body{width:1070px;height:1200px;overflow:hidden}
body{position:relative;background:repeating-linear-gradient(45deg,#1b1b1b 0 2px,#141414 2px 4px);font-family:"Arimo",Arial,sans-serif;color:var(--text)}
.abs{position:absolute}
.page{left:153px;top:18px;width:765px;height:916px;background:var(--page)}
.logo{display:flex;align-items:center;gap:8px;white-space:nowrap}
.logo .mark{width:50px;height:50px;border-radius:50%;background:var(--navy);flex:none}
.logo .name{font-family:"Tinos",Georgia,serif;font-size:22px;color:var(--navy);letter-spacing:.5px}
.logo.small{gap:6px}
.logo.small .mark{width:36px;height:36px}
.logo.small .name{font-size:12px;letter-spacing:0}
.social{left:818px;top:46px;display:flex;gap:4px}
.social span{width:26px;height:26px;border-radius:4px;background:var(--navy)}
.social span:first-child{background:var(--red)}
.nav{left:169px;top:98px;width:733px;height:36px;background:var(--navy);border-radius:6px;display:flex;align-items:center;overflow:hidden}
.nav a{font-family:"Tinos",Georgia,serif;color:#fff;text-decoration:none;font-size:13px;padding:0 14px;border-left:1px solid #2a3572;line-height:14px}
.nav a.home{background:var(--red);height:36px;line-height:36px;width:74px;text-align:center;padding:0;border:none}
.nav a.first{border-left:none}
.slider{left:167px;top:140px;width:736px;height:279px;background:#fff;border:1px solid var(--line)}
.slide-img{left:174px;top:146px;width:723px;height:267px;background:radial-gradient(circle at 12% 25%,#f3ecd8 0,#b59d74 8%,#6d5a3f 40%,#3a2e22 80%)}
.slide-ctrl{left:819px;top:337px;width:65px;height:31px;background:rgba(14,24,80,.85);display:flex;align-items:center;justify-content:center}
.caption{left:174px;top:368px;width:723px;height:45px;background:rgba(14,24,80,.88);color:#fff;font-family:"Tinos",Georgia,serif;font-size:11.5px;line-height:13.5px;padding:9px 14px}
h2{font-family:"Tinos",Georgia,serif;font-weight:400;color:var(--navy);font-size:14.5px;letter-spacing:.2px}
.card{left:167px;width:487px;height:200px;background:var(--panel);border:1px solid var(--line)}
.thumb{width:114px;height:113px;background:linear-gradient(135deg,#3a2224,#6b4a4c 50%,#2a1618)}
.btn{width:112px;height:25px;border-radius:3px;color:#fff;font-size:11px;display:flex;align-items:center;justify-content:center}
.btn.red{background:linear-gradient(#c42525,var(--red-dark))}
.btn.blue{background:linear-gradient(#1a2560,var(--navy-dark))}
.box{width:353px;background:#f6f6f6;border:1px solid var(--line);padding:10px 12px}
.box h3{font-family:"Tinos",Georgia,serif;font-weight:400;color:var(--red);font-size:11.5px;margin-bottom:7px}
.box p{font-size:9.5px;line-height:13.6px;color:var(--text)}
.box h4{font-family:"Tinos",Georgia,serif;font-weight:400;color:var(--red);font-size:11.5px;margin-bottom:8px}
.meta{display:grid;grid-template-columns:55px 8px 1fr;font-size:9.5px;line-height:15px}
.meta dt{font-family:"Tinos",Georgia,serif;color:var(--red);font-size:10px}
.pager{left:167px;top:898px;display:flex;gap:7px;align-items:center;font-size:12px;color:var(--muted)}
.pager span{width:17px;height:17px;display:flex;align-items:center;justify-content:center}
.pager .on,.pager .next{background:var(--red);color:#fff}
.side{left:676px;top:428px;width:226px;height:485px;background:var(--panel);border:1px solid var(--line)}
.signup{left:692px;top:466px;width:196px;height:32px;border:1px solid var(--line);border-radius:4px;background:#f7f7f7}
.signup .field{left:5px;top:4px;width:120px;height:22px;background:#fff;border:1px solid #c8c8c8;border-radius:3px;font-size:9.5px;color:#777;padding:5px 10px}
.signup .go{left:129px;top:3px;width:60px;height:24px;background:var(--red);border-radius:3px;color:#fff;font-size:10px;display:flex;align-items:center;justify-content:center}
.dash{left:686px;width:208px;border-top:1px dashed #bdbdbd}
.video{left:691px;top:549px;width:197px;height:153px;background:#fff;border:1px solid var(--line)}
.video .still{left:4px;top:4px;width:187px;height:143px;background:linear-gradient(135deg,#bdbdbd,#6f6f6f 55%,#9a9a9a)}
.play{width:54px;height:54px;border-radius:50%;background:#fff;display:flex;align-items:center;justify-content:center}
.bubble{left:694px;top:758px;width:192px;height:96px;background:#d6d6d6;border-radius:8px;padding:14px 16px;font-size:9.3px;line-height:13.8px;color:#555}
.by{left:815px;top:870px;font-size:9.5px;line-height:13.5px}
.by b{font-weight:400;color:var(--red)}
.flinks{display:grid;grid-template-columns:123px 123px;column-gap:15px}
.flinks a{display:flex;align-items:center;gap:6px;height:27px;border-bottom:1px solid #9a9a9a;color:#cfcfcf;font-size:10px;text-decoration:none}
.flinks a i{color:var(--red);font-style:normal;font-size:8px}
.fhead{font-family:"Tinos",Georgia,serif;color:var(--red);font-size:14px}
.addr{font-size:9.8px;line-height:15px;color:#cfcfcf}
.addr em{font-style:normal;color:var(--red)}
.qc{font-size:9.8px;color:#cfcfcf}
.inp{background:#fff;border-radius:2px}
.submit{left:819px;top:1073px;width:83px;height:24px;background:var(--red);border-radius:3px;color:#fff;font-size:10.5px;display:flex;align-items:center;justify-content:center}
.strip{left:153px;top:1108px;width:765px;height:74px;background:var(--page)}
.copy{left:168px;top:1139px;font-size:9.8px;color:#333}
.badge{background:#222}
</style>
</head>
<body>
<div class="abs page"></div>

<div class="abs logo" style="left:168px;top:32px"><span class="mark"></span><span class="name">BRAMBLEWICK</span></div>
<div class="abs social"><span></span><span></span><span></span></div>

<nav class="abs nav">
  <a class="home">Home</a>
  <a class="first">Upcoming Auctions</a><a>Auction Results</a><a>Sell or Consign</a><a>About Us</a><a>Services</a><a>FAQ</a><a>Contact Us</a>
</nav>

<div class="abs slider"></div>
<div class="abs slide-img" role="img" aria-label="Photo of graded coins in holders on a display tray"></div>
<div class="abs slide-ctrl">
  <svg width="40" height="14" viewBox="0 0 40 14"><rect x="2" y="1" width="3" height="12" fill="#fff"/><rect x="7" y="1" width="3" height="12" fill="#fff"/><path d="M22 2l-5 5 5 5M30 2l5 5-5 5" stroke="#fff" stroke-width="2.4" fill="none"/></svg>
</div>
<div class="abs caption">Lorem Ipsum is simply dummy text of the printing and typesetting industry. Lorem Ipsum has been the industry's standard dummy text ever since the 1500s, when an unand typesetting industry. Lorem Ipsum has been the industry's standard ..</div>

<h2 class="abs" style="left:167px;top:444px">FEATURED AUCTIONS</h2>

<div class="abs card" style="top:466px"></div>
<div class="abs thumb" style="left:174px;top:474px" role="img" aria-label="Photo of coins in a display case"></div>
<div class="abs btn red" style="left:175px;top:592px">Details</div>
<div class="abs btn blue" style="left:175px;top:621px">Videos</div>
<div class="abs box" style="left:294px;top:474px;height:94px"><h3>CONTRARY TO POPULAR BELIEF</h3><p>Lorem Ipsum is simply dummy text of the printing and typesetting industry. Lorem Ipsum has been the industry's standard dummy text ever since the 1500s, when an unknown printer took a galley of type and scrambled it to make..</p></div>
<div class="abs box" style="left:294px;top:575px;height:84px"><h4>Live On-Site Auction</h4><dl class="meta"><dt>Begins</dt><dd>:</dd><dd>Saturday, July 13, 2013 at 1:00 PM EDT</dd><dt>Ends</dt><dd>:</dd><dd>Saturday, July 13, 2013 at 2:00 PM EDT</dd><dt>Location</dt><dd>:</dd><dd>418 Larkspur Court drive, Fenmoor, OH 43790</dd></dl></div>

<div class="abs card" style="top:683px"></div>
<div class="abs thumb" style="left:174px;top:691px" role="img" aria-label="Photo of coins in a display case"></div>
<div class="abs btn red" style="left:175px;top:809px">Details</div>
<div class="abs btn blue" style="left:175px;top:838px">Photos</div>
<div class="abs box" style="left:294px;top:691px;height:94px"><h3>CONTRARY TO POPULAR BELIEF</h3><p>Lorem Ipsum is simply dummy text of the printing and typesetting industry. Lorem Ipsum has been the industry's standard dummy text ever since the 1500s, when an unknown printer took a galley of type and scrambled it to make..</p></div>
<div class="abs box" style="left:294px;top:792px;height:84px"><h4>Live On-Site Auction</h4><dl class="meta"><dt>Begins</dt><dd>:</dd><dd>Saturday, July 13, 2013 at 1:00 PM EDT</dd><dt>Ends</dt><dd>:</dd><dd>Saturday, July 13, 2013 at 2:00 PM EDT</dd><dt>Location</dt><dd>:</dd><dd>418 Larkspur Court drive, Fenmoor, OH 43790</dd></dl></div>

<div class="abs pager"><span class="on">1</span><span>2</span><span>3</span><span>4</span><span>5</span><span>6</span><span class="next"><svg width="8" height="10" viewBox="0 0 8 10"><path d="M2 1l4 4-4 4" stroke="#fff" stroke-width="2" fill="none"/></svg></span></div>

<aside class="abs side"></aside>
<h2 class="abs" style="left:691px;top:444px">SIGN UP TO E-MAIL</h2>
<div class="abs signup"><div class="abs field">Email</div><div class="abs go">Sign Up</div></div>
<div class="abs dash" style="top:516px"></div>
<h2 class="abs" style="left:691px;top:529px">FEATURED VIDEO</h2>
<div class="abs video"><div class="abs still" role="img" aria-label="Video still of coins in a display case"></div>
  <div class="abs play" style="left:71px;top:49px"><svg width="18" height="20" viewBox="0 0 18 20"><path d="M2 1l15 9-15 9z" fill="var(--red)"/></svg></div></div>
<div class="abs dash" style="top:716px"></div>
<h2 class="abs" style="left:691px;top:730px">CLIENT TESTIMONIALS</h2>
<svg class="abs" style="left:869px;top:732px" width="22" height="12" viewBox="0 0 22 12"><path d="M8 1L3 6l5 5" stroke="var(--red)" stroke-width="2.5" fill="none"/><path d="M14 1l5 5-5 5" stroke="#999" stroke-width="2.5" fill="none"/></svg>
<div class="abs bubble">Lorem Ipsum is simply dummy text of the printing and typesetting industry. Lorem Ipsum has been the industry's standard dummy text ever printer tookscrambled.</div>
<svg class="abs" style="left:832px;top:853px" width="22" height="12" viewBox="0 0 22 12"><path d="M0 0h22L20 12z" fill="#d6d6d6"/></svg>
<div class="abs by"><b>By</b><br>Prof: Adler Quinn</div>

<div class="abs flinks" style="left:169px;top:953px">
  <a><i>→</i>Home</a><a><i>→</i>Upcoming Auctions</a>
  <a><i>→</i>Auction Results</a><a><i>→</i>Sell or Consign</a>
  <a><i>→</i>About Us</a><a><i>→</i>Services</a>
  <a><i>→</i>FAQ</a><a><i>→</i>Contact Us</a>
</div>

<div class="abs fhead" style="left:490px;top:953px">Address</div>
<div class="abs addr" style="left:491px;top:979px">Door No.<br>Street Address<br>Country<br>Mail to : <em>info@bramblewick.com</em><br>Call Us : <em>+01 22 5678 90</em></div>

<div class="abs fhead" style="left:675px;top:953px">Quick Contact</div>
<div class="abs qc" style="left:675px;top:983px">Name</div><div class="abs qc" style="left:729px;top:983px">:</div>
<div class="abs qc" style="left:675px;top:1006px">Email</div><div class="abs qc" style="left:729px;top:1006px">:</div>
<div class="abs qc" style="left:675px;top:1028px">Comment</div><div class="abs qc" style="left:729px;top:1028px">:</div>
<div class="abs inp" style="left:748px;top:978px;width:154px;height:20px"></div>
<div class="abs inp" style="left:748px;top:1002px;width:154px;height:19px"></div>
<div class="abs inp" style="left:748px;top:1025px;width:154px;height:41px"></div>
<div class="abs submit">SUBMIT</div>

<div class="abs strip"></div>
<div class="abs copy">2013 © Bramblewick. All rights Reserved.&nbsp; Privacy Policy &nbsp;|&nbsp; Terms &amp; Conditions</div>
<div class="abs logo small" style="left:576px;top:1127px"><span class="mark"></span><span class="name">BRAMBLEWICK</span></div>
<div class="abs badge" style="left:730px;top:1130px;width:38px;height:31px"></div>
<div class="abs badge" style="left:772px;top:1130px;width:130px;height:31px"></div>
</body>
</html>
```